Lightweight, clean Wordpress theme for fitness app website

Fit-Sprocket.com needs a new website.

Fit-Sprocket itself is a mobile fitness app and this website will support it and help to promote it with screenshots and descriptions of the app.

Attached is the logo. The main colours are the blue and white on the logo.

I need a fully functioning Wordpress theme for this website.

It needs to be clean, lightweight, fast loading and easy to maintain and build.
The theme should include the home page, pages and posts so that we can have the flexibility to do what we want.

It should work just as well on mobile as for desktop.

The target audience is all fitness lovers, female and male, any age.

Must Have:
- Wordpress theme.
- Pages, posts and a home page.
- Simple, clean & lightweight.
- Desktop & mobile styling
- See attachment for colours and fonts

Should Not Have:
- Bloated & slow loading designs

Target Market(s)

Fitness enthusiasts of all abilities.
Male / Female. Young & Old.
Should NOT use imagery of big body builders.

Industry/Entity Type

Fitness

Coding

Coded - Design and coding required

Number of Pages Required

3 page

Requirements
Must have
• Wordpress theme
• Landing / home page.
• Template for a page and a post.
• Simple, clean & fast loading.

```html
<!DOCTYPE html>
<html lang="en">
<head>
<meta charset="utf-8">
<title>Fit-Sprocket.com — Online Personal Training</title>
<link href="https://fonts.googleapis.com/css2?family=Exo+2:wght@300;400;500&family=Open+Sans:wght@400;600;700&family=Montserrat:wght@400;600&display=swap" rel="stylesheet">
<style>
:root{
  --blue:#22a7e0;
  --blue-dark:#1a8fc4;
  --ink:#222;
  --text:#666;
  --dark:#1b1b1b;
  --dark-2:#2e2e2e;
  --light:#f4f4f4;
  --white:#fff;
}
*{box-sizing:border-box;margin:0;padding:0}
html,body{width:1200px;height:3429px;overflow:hidden}
body{position:relative;background:var(--white);font-family:"Open Sans",sans-serif;color:var(--text)}
.abs{position:absolute}
.heading{font-family:"Exo 2",sans-serif;font-weight:400}

/* top bar */
.topbar{left:0;top:0;width:1200px;height:34px;background:var(--dark);color:#fff;font-size:13px}
.topbar .mail{position:absolute;right:100px;top:9px;display:flex;align-items:center;gap:7px}

/* nav */
.nav{left:0;top:34px;width:1200px;height:80px;background:#fff}
.brand{display:flex;align-items:center;gap:12px;font-family:"Exo 2",sans-serif;font-size:27px;color:#333;font-weight:400}
.brand .dot{width:34px;height:34px;border-radius:50%;background:var(--blue)}
.nav .brand{position:absolute;left:98px;top:22px}
.menu{position:absolute;left:565px;top:0;height:80px;display:flex;font-size:14px;font-family:"Open Sans",sans-serif;color:#444;text-transform:uppercase}
.menu a{display:flex;align-items:center;height:80px;padding:0 17px;color:#444;text-decoration:none}
.menu a.active{background:var(--blue);color:#fff;width:73px;justify-content:center;padding:0}
.menu a:nth-child(2){margin-left:58px}
.menu a:nth-child(3){margin-left:14px}
.menu a:nth-child(4){margin-left:14px}
.menu a:nth-child(5){margin-left:22px}

/* hero */
.hero{left:0;top:114px;width:1200px;height:606px;background:radial-gradient(ellipse 320px 420px at 600px 150px,#5a5654 0%,#2e2c2b 45%,#141414 100%)}
.hero h1{position:absolute;top:236px;width:100%;text-align:center;color:#fff;font-size:44px;line-height:54px;font-family:"Exo 2",sans-serif;font-weight:400;letter-spacing:1px}
.hero p{position:absolute;top:294px;width:100%;text-align:center;color:#eee;font-size:16px;line-height:22px}
.btn{display:inline-flex;align-items:center;justify-content:center;background:var(--blue);color:#fff;font-size:14px;height:36px}
.hero .btn{position:absolute;left:549px;top:339px;width:121px}

/* features */
.feature-panel{left:377px;top:620px;width:725px;height:153px;background:#fff;box-shadow:0 3px 8px rgba(0,0,0,.2);display:flex}
.feature{flex:1;position:relative;text-align:center;color:var(--blue);font-size:13px;font-weight:700;text-transform:uppercase}
.feature svg{position:absolute;left:50%;top:32px;transform:translateX(-50%)}
.feature span{position:absolute;left:0;right:0;top:92px}
.feature i{position:absolute;left:50%;bottom:0;width:22px;height:4px;margin-left:-11px;background:var(--blue)}
.feature-main{left:98px;top:608px;width:279px;height:179px;background:var(--blue);color:#fff;font-size:13px;font-weight:700;text-align:center;box-shadow:0 3px 8px rgba(0,0,0,.2)}
.feature-main span{position:absolute;left:0;right:0;top:103px}
.feature-badge{left:187px;top:560px;width:92px;height:92px;border-radius:50%;background:#fff;box-shadow:0 0 0 8px rgba(255,255,255,.4)}
.feature-badge div{position:absolute;left:13px;top:13px;width:66px;height:66px;border-radius:50%;background:var(--blue)}

/* about */
.about{left:0;top:830px;width:1200px;text-align:center}
.section-title{font-family:"Exo 2",sans-serif;font-weight:300;font-size:36px}
.about .section-title{color:var(--blue);letter-spacing:2px}
.about h3{margin-top:20px;font-size:18px;color:#222;font-weight:600}
.about p{width:1000px;margin:14px auto 0;font-size:13.5px;line-height:23px;color:#777}
.about .actions{margin-top:44px;display:flex;justify-content:center;gap:25px}
.about .btn{width:120px}
.btn-ghost{display:inline-flex;align-items:center;justify-content:center;width:110px;height:36px;border:1px dashed #ccc;font-size:14px;color:#333}

/* weight */
.weight{left:0;top:1246px;width:1200px;height:452px;background:linear-gradient(90deg,#3a3331 0%,#2a2625 35%,#262626 55%,#1f1f1f 100%)}
.weight .photo{position:absolute;left:0;top:0;width:520px;height:452px;background:radial-gradient(ellipse 220px 260px at 240px 200px,rgba(180,130,110,.35),rgba(0,0,0,0) 70%)}
.weight h2{position:absolute;top:36px;width:100%;text-align:center;color:#fff;font-size:31px}
.gender{position:absolute;left:485px;top:121px;display:flex}
.gender span{width:112px;height:46px;background:var(--blue);color:#fff;font-size:14px;display:flex;align-items:center;justify-content:center;border-right:1px solid #8fd3f0}
.calc{position:absolute;left:288px;top:233px;width:624px;height:64px;background:var(--blue);color:#fff;font-size:16px}
.calc label{position:absolute;left:30px;top:21px}
.calc .input{position:absolute;left:183px;top:16px;width:180px;height:34px;background:#fff;color:#aaa;font-size:13px;padding:9px 10px}
.calc .unit{position:absolute;left:410px;top:16px;width:130px;height:34px;border-bottom:1px solid #fff;text-align:center;padding-top:8px;font-size:15px}

/* experts */
.experts-title{left:0;top:1735px;width:1200px;text-align:center;color:#333;font-size:33px}
.expert{top:1842px;width:226px;height:307px;background:linear-gradient(180deg,#5a5a5a,#2a2a2a)}
.expert.warm{background:linear-gradient(180deg,#6e5c50,#2f2824)}
.expert-name{position:absolute;left:0;right:0;top:172px;text-align:center;color:#fff}
.expert-name b{display:block;font-family:"Montserrat",sans-serif;font-weight:600;font-size:19px}
.expert-name small{font-size:11px;color:#ddd}
.social{position:absolute;left:0;bottom:0;width:100%;height:51px;background:var(--blue);display:flex;justify-content:space-around;align-items:center;padding:0 28px}
.social i{width:8px;height:8px;border-radius:50%;background:#fff;display:block}

/* testimonials */
.testimonials{left:0;top:2240px;width:1200px;height:494px;background:linear-gradient(180deg,#3b3b3b,#2b2b2b)}
.testimonials h2{position:absolute;top:36px;width:100%;text-align:center;color:#fff;font-size:33px}
.t-card{top:185px;width:306px;height:222px;background:#fff;border-radius:3px;text-align:center}
.t-card h4{margin-top:46px;font-family:"Montserrat",sans-serif;font-weight:600;font-size:16px;color:#333}
.t-card p{width:262px;margin:20px auto 0;font-size:12px;line-height:17px;color:#555}
.t-card a{display:block;margin-top:14px;color:var(--blue);font-size:13px;text-decoration:none}
.avatar{position:absolute;left:103px;top:-58px;width:100px;height:100px;border-radius:50%;background:rgba(255,255,255,.12)}
.avatar div{position:absolute;left:13px;top:13px;width:74px;height:74px;border-radius:50%;border:3px solid #fff;background:linear-gradient(160deg,#c9b7a6,#6b5a4e)}

/* newsletter */
.newsletter{left:0;top:2734px;width:1200px;height:226px;background:linear-gradient(180deg,#efefef,#f7f7f7)}
.newsletter .kicker{position:absolute;left:100px;top:79px;font-size:11px;letter-spacing:2px;color:#444;text-transform:uppercase}
.newsletter h2{position:absolute;left:98px;top:96px;font-family:"Montserrat",sans-serif;font-weight:400;font-size:29px;color:#333}
.newsletter h2 b{font-weight:600}
.newsletter .field{position:absolute;left:437px;top:82px;width:473px;height:48px;border-radius:24px;background:#fff;font-size:12px;color:#999;padding:16px 30px}
.newsletter .send{position:absolute;left:937px;top:82px;width:165px;height:48px;border-radius:24px;background:var(--blue);color:#fff;font-size:15px;display:flex;align-items:center;justify-content:center;gap:8px}

/* footer */
.footer{left:0;top:2960px;width:1200px;height:359px;background:var(--light)}
.footer .brand{position:absolute;left:103px;top:40px}
.footer .about-text{position:absolute;left:110px;top:145px;width:300px;font-size:12.5px;line-height:20px;color:#555}
.contact{position:absolute;left:110px;top:218px;font-size:12px;color:#333;line-height:25px}
.contact div{display:flex;align-items:center;gap:10px}
.contact .link{color:var(--blue)}
.col{position:absolute;top:80px;font-size:13px;color:#333}
.col h5{font-size:13px;font-weight:400}
.col h5 b{font-weight:700}
.col .rule{width:26px;height:2px;background:var(--blue);margin:22px 0 12px}
.col li{list-style:none;font-size:12px;color:#666;line-height:27px;display:flex;align-items:center;gap:9px}
.col li::before{content:"";width:10px;height:10px;border-radius:50%;border:1px solid #ccc}
.app-box{position:absolute;left:782px;top:112px;width:308px;height:170px;background:#fff;text-align:center}
.app-box h4{margin-top:20px;font-family:"Exo 2",sans-serif;font-weight:400;font-size:28px;color:#333}
.app-box .store{width:256px;height:82px;margin:18px auto 0;background:#111;border-radius:8px}
.footer-bump{left:530px;top:3280px;width:140px;height:40px}
.copyright{left:0;top:3319px;width:1200px;height:110px;background:#fff;text-align:center;font-size:13px;color:#333;padding-top:48px}
</style>
</head>
<body>

<div class="abs topbar">
  <div class="mail">
    <svg width="14" height="10" viewBox="0 0 14 10"><rect width="14" height="10" fill="#fff"/><path d="M0 0l7 6 7-6" stroke="#1b1b1b" fill="none"/></svg>
    info@fit-sprocket.com
  </div>
</div>

<header class="abs nav">
  <div class="brand"><span class="dot"></span>Fit-Sprocket.com</div>
  <nav class="menu">
    <a class="active">Home</a><a>About Us</a><a>Blog</a><a>The App</a><a>Contact Us</a>
  </nav>
</header>

<section class="abs hero" role="img" aria-label="Photo of an athlete seen from behind with arms spread, on a dark background">
  <h1>Online Personal Training</h1>
  <p>Maximum Results in Minimum Time, no matter your location</p>
  <span class="btn">View More</span>
</section>

<div class="abs feature-panel">
  <div class="feature">
    <svg width="34" height="30" viewBox="0 0 34 30"><circle cx="22" cy="8" r="4" fill="#22a7e0"/><path d="M4 16l10-5 8 6M2 24c5-3 10 3 15 0s10 3 15 0" stroke="#22a7e0" stroke-width="3" fill="none"/></svg>
    <span>Best Service</span><i></i>
  </div>
  <div class="feature">
    <svg width="30" height="30" viewBox="0 0 30 30"><g fill="#22a7e0"><circle cx="9" cy="6" r="3"/><circle cx="18" cy="6" r="3"/><circle cx="24" cy="13" r="3"/><circle cx="15" cy="14" r="3"/><circle cx="7" cy="17" r="3"/><circle cx="17" cy="24" r="3"/></g></svg>
    <span>Price Options</span><i></i>
  </div>
  <div class="feature">
    <svg width="28" height="32" viewBox="0 0 28 32"><g fill="#22a7e0"><circle cx="14" cy="5" r="4"/><rect x="10" y="11" width="8" height="12"/><rect x="2" y="15" width="5" height="15"/><rect x="21" y="15" width="5" height="15"/><rect x="10" y="24" width="8" height="6"/></g></svg>
    <span>Special Offer</span><i></i>
  </div>
</div>
<div class="abs feature-main"><span>REAL RESULTS</span></div>
<div class="abs feature-badge"><div>
  <svg width="66" height="66" viewBox="0 0 66 66"><circle cx="33" cy="22" r="4" fill="#fff"/><path d="M20 30l13-2 13 2M33 28v12l-6 10M33 40l6 10" stroke="#fff" stroke-width="3" fill="none" stroke-linecap="round"/></svg>
</div></div>

<section class="abs about">
  <h2 class="section-title">ABOUT US</h2>
  <h3>Lorem Ipsum is simply dummy text of the printing and typesetting industry</h3>
  <p>Lorem Ipsum has been the industry's standard dummy text ever since the 1500s, when an unknown printer took a galley of type and scrambled it to make a type specimen book. It has survived not only five centuries, but also the leap into electronic typesetting, remaining essentially unchanged. It was popularised in the 1960s with the release of Typeline sheets containing Lorem Ipsum passages, and more recently with desktop publishing software like Pagemill Desk including versions of Lorem Ipsum Lorem Ipsum has been the industry's standard dummy text ever since the 1500s, when an unknown printer took a galley of type and scrambled it to make a type specimen book. It has survived not only five centuries, but also the leap into electronic typesetting.</p>
  <div class="actions"><span class="btn">View More</span><span class="btn-ghost">About Us</span></div>
</section>

<section class="abs weight">
  <div class="photo" role="img" aria-label="Photo of a woman training with a barbell"></div>
  <h2 class="heading">Find your ideal weight:</h2>
  <div class="gender"><span>FOR FEMALE</span><span>FOR MALE</span></div>
  <div class="calc">
    <label>Your height, ft:</label>
    <div class="input">Input Height</div>
    <div class="unit">LBS</div>
  </div>
</section>

<h2 class="abs heading experts-title">Meet Our Expert</h2>
<div class="abs expert" style="left:103px" role="img" aria-label="Portrait photo of a fitness trainer">
  <div class="expert-name"><b>Marco Delvane</b><small>Fitness Trainer</small></div>
  <div class="social"><i></i><i></i><i></i><i></i></div>
</div>
<div class="abs expert warm" style="left:352px" role="img" aria-label="Photo of a male trainer in a gym"></div>
<div class="abs expert" style="left:603px" role="img" aria-label="Photo of a female trainer holding a barbell"></div>
<div class="abs expert warm" style="left:855px" role="img" aria-label="Photo of a male trainer in shorts"></div>

<section class="abs testimonials" role="img" aria-label="Dimmed gym interior photo behind testimonials">
  <h2 class="heading">Our Testimonials</h2>
  <div class="abs t-card" style="left:112px">
    <div class="avatar" role="img" aria-label="Client portrait"><div></div></div>
    <h4>Owen Castelli</h4>
    <p>This is Pixelshop's version of Lorem Ipsum. Proin gravida nibh vel velit auctor aliquet. Aenean sollicitudin, lorem quis bibendum auctor, nisi elit consequat ipsum, nec</p>
    <a>Read more</a>
  </div>
  <div class="abs t-card" style="left:446px">
    <div class="avatar" role="img" aria-label="Client portrait"><div></div></div>
    <h4>Jonas Pirrell</h4>
    <p>This is Pixelshop's version of Lorem Ipsum. Proin gravida nibh vel velit auctor aliquet. Aenean sollicitudin, lorem quis bibendum auctor, nisi elit consequat ipsum, nec</p>
    <a>Read more</a>
  </div>
  <div class="abs t-card" style="left:780px">
    <div class="avatar" role="img" aria-label="Client portrait"><div></div></div>
    <h4>Dana Wexley</h4>
    <p>This is Pixelshop's version of Lorem Ipsum. Proin gravida nibh vel velit auctor aliquet. Aenean sollicitudin, lorem quis bibendum auctor, nisi elit consequat ipsum, nec</p>
    <a>Read more</a>
  </div>
</section>

<section class="abs newsletter">
  <div class="kicker">Join our newsletter</div>
  <h2>subscribe <b>newsletter</b></h2>
  <div class="field">enter your email address</div>
  <div class="send">subscribe
    <svg width="14" height="10" viewBox="0 0 14 10"><path d="M0 5h11M8 1l4 4-4 4" stroke="#fff" stroke-width="2" fill="none"/></svg>
  </div>
</section>

<footer class="abs footer">
  <div class="brand"><span class="dot"></span>Fit-Sprocket.com</div>
  <p class="about-text">Lorem ipsum dolor sit amet, consectetuer adipiscing elit, sed diam nonummy nibh euismod tincidunt ut laoreet dolore magna.</p>
  <div class="contact">
    <div><svg width="10" height="12" viewBox="0 0 10 12"><path d="M5 12C1 7 0 5 0 5a5 5 0 0110 0s-1 2-5 7z" fill="#333"/><circle cx="5" cy="5" r="2" fill="#f4f4f4"/></svg><span><b>42 ridgeway lane, westbrook</b>, united state</span></div>
    <div><svg width="11" height="11" viewBox="0 0 11 11"><rect x=".5" y=".5" width="10" height="10" fill="none" stroke="#333"/><path d="M3 3h5M3 5.5h5M3 8h3" stroke="#333"/></svg>contact@fit-sprocket.com</div>
    <div><svg width="11" height="11" viewBox="0 0 11 11"><rect width="11" height="11" fill="#333"/><path d="M1 2l4.5 4L10 2" stroke="#fff" fill="none"/></svg><span class="link">info@fit-sprocket.com</span></div>
  </div>
  <div class="col" style="left:446px">
    <h5><b>Fitness</b> information</h5>
    <div class="rule"></div>
    <ul><li>about our shop</li><li>top Sellers</li><li>our blog</li><li>New Product</li><li>Secure Shopping</li></ul>
  </div>
  <div class="col" style="left:615px">
    <h5><b>my</b> account</h5>
    <div class="rule"></div>
    <ul><li>my account</li><li>discount</li><li>personal information</li><li>my address</li><li>order history</li></ul>
  </div>
  <div class="app-box">
    <h4>Get An App</h4>
    <div class="store" role="img" aria-label="App store download badge"></div>
  </div>
</footer>
<svg class="abs footer-bump" viewBox="0 0 140 40"><path d="M0 40C30 40 40 8 70 8s40 32 70 32z" fill="#fff"/><circle cx="70" cy="24" r="7" fill="none" stroke="#bbb"/><path d="M66 25l4-4 4 4" stroke="#bbb" fill="none"/></svg>

<div class="abs copyright">Copyright © 2017 fit-sprocket.com, All Right Reserved</div>

</body>
</html>
```